Pillow Company needs Pillow Insert Design

I just started a new pillow line with two pillow types. I have a hotel pillow and an organic pillow. I need two pillow insert signs designed that follow the same layout but are different color types. I want one sign to incorporate silver and white look and another sign to incorporate a green and white look (this one to look organic). They must have the same layout but different colors. I have include examples of what I want it to look like. In addition, I have uploaded the two hi res images for each sign. My logo is uploaded too.

I am open to other concepts and colors as long as it looks modern, clean and upscale. In addition, I need a Made in the USA logo on the pillow insert designs.

I have attached details on sign, images to be used, and examples that I like.

The Pillow Sign Size is 12 inches x 12 inches.

```html
<!DOCTYPE html>
<html lang="en">
<head>
<meta charset="utf-8">
<title>LunaRest Alternative Down Pillow Insert</title>
<link rel="stylesheet" href="https://fonts.googleapis.com/css2?family=Great+Vibes&family=Lora:wght@400;700&display=swap">
<style>
  :root {
    --backdrop: #1e1e1e;
    --paper: #ffffff;
    --tint: #eef6e6;
    --leaf: #74b43c;
    --leaf-light: #8fcb4f;
    --leaf-deep: #4f9128;
    --forest: #1c7431;
    --ink-green: #1f6a2d;
    --photo-light: #f4f1ec;
    --photo-mid: #e2d6c8;
  }
  * { box-sizing: border-box; margin: 0; padding: 0; }
  html, body { width: 1200px; height: 1000px; overflow: hidden; background: var(--backdrop); }
  .canvas { position: relative; width: 1200px; height: 1000px; }
  .insert {
    position: absolute; left: 155px; top: 52px; width: 905px; height: 905px;
    background:
      radial-gradient(ellipse at 80% 15%, var(--tint) 0%, rgba(238,246,230,0) 45%),
      radial-gradient(ellipse at 10% 85%, var(--tint) 0%, rgba(238,246,230,0) 40%),
      radial-gradient(ellipse at 95% 80%, var(--tint) 0%, rgba(238,246,230,0) 35%),
      var(--paper);
    overflow: hidden;
    font-family: "Lora", Georgia, serif;
  }
  .brand { position: absolute; left: 8px; top: 8px; display: flex; align-items: center; gap: 18px; }
  .brand-square { width: 92px; height: 78px; background: var(--leaf); border-radius: 4px; }
  .brand-name { font-family: "Lora", Georgia, serif; font-weight: 700; font-size: 40px; color: var(--leaf); letter-spacing: 0.5px; }
  .title {
    position: absolute; right: 10px; top: 100px;
    font-family: "Great Vibes", cursive; font-size: 54px; color: var(--forest); white-space: nowrap;
  }
  .band {
    position: absolute; left: 0; top: 271px; width: 905px; height: 117px;
    background: linear-gradient(180deg, var(--leaf-light) 0%, var(--leaf) 45%, var(--leaf-deep) 100%);
  }
  .band-copy {
    position: absolute; left: 480px; top: 27px; width: 440px; text-align: center;
    color: var(--paper); font-size: 17.5px; line-height: 28px;
  }
  .band-copy strong { font-weight: 700; }
  .hero { position: absolute; left: 0; top: 108px; }
  .tagline {
    position: absolute; right: 14px; top: 445px;
    font-family: "Great Vibes", cursive; font-size: 40px; color: var(--forest); white-space: nowrap;
  }
  .intro {
    position: absolute; left: 20px; top: 540px; width: 865px; text-align: center;
    color: var(--leaf); font-weight: 700; font-size: 17.5px; line-height: 27px;
  }
  .features {
    position: absolute; left: 215px; top: 634px; list-style: none;
    color: var(--ink-green); font-size: 17.5px; line-height: 28.5px;
  }
  .features li::before { content: "\2022"; margin-right: 8px; }
  .footer-note {
    position: absolute; left: 358px; top: 876px;
    color: var(--leaf); font-weight: 700; font-size: 13.5px;
  }
  .badges { position: absolute; left: 660px; top: 840px; }
</style>
</head>
<body>
<div class="canvas">
  <section class="insert">
    <div class="brand">
      <span class="brand-square"></span>
      <span class="brand-name">LunaRest</span>
    </div>

    <h1 class="title">Alternative Down Pillow</h1>

    <div class="band">
      <p class="band-copy">This pillow was designed to give you<br>the most comfortable night’s sleep in your life.<br><strong>Designed for all types of sleep positions.</strong></p>
    </div>

    <svg class="hero" width="520" height="430" viewBox="0 0 520 430">
      <defs>
        <linearGradient id="ring-fill" x1="0" y1="0" x2="1" y2="1">
          <stop offset="0" stop-color="#9ad35a"/>
          <stop offset="0.5" stop-color="#6cad35"/>
          <stop offset="1" stop-color="#3f8420"/>
        </linearGradient>
        <radialGradient id="photo-fill" cx="0.5" cy="0.4" r="0.6">
          <stop offset="0" stop-color="#e6d8c9"/>
          <stop offset="0.55" stop-color="#f2eee9"/>
          <stop offset="1" stop-color="#fbfbfa"/>
        </radialGradient>
      </defs>
      <circle cx="250" cy="215" r="213" fill="url(#ring-fill)"/>
      <circle cx="250" cy="215" r="198" fill="#ffffff"/>
      <circle cx="250" cy="215" r="193" fill="url(#photo-fill)" role="img" aria-label="Photo of a smiling couple relaxing together in a white bed with breakfast on a tray"/>
    </svg>

    <p class="tagline">Surround Yourself with the Best!</p>

    <p class="intro">We added revolutionary features from our advanced Super Soft Premium Memory Foam<br>that has an open cell structure design that recovers quickly and does not trap heat to our gel<br>infused polyester fiber to our 100% Certified Organic Cotton Fabric.</p>

    <ul class="features">
      <li>Made From the Finest Premium Materials</li>
      <li>Adjusts to your Body Weight and Temperature</li>
      <li>100% Certified Organic Cotton Fabric</li>
      <li>Cool Non-Allergenic, Anti-Microbial, and Hypoallergenic</li>
      <li>Conforms to Head and Neck for optimal Alignment during Sleep</li>
      <li>Mildew Proof and Dust Mite Resistant</li>
      <li>VerdaFoam ® toxin free certified foam</li>
    </ul>

    <p class="footer-note">Individually Handcrafted and Made in USA</p>

    <svg class="badges" width="240" height="65" viewBox="0 0 240 65">
      <rect x="5" y="12" width="67" height="40" fill="#c9cfd8"/>
      <circle cx="125" cy="31" r="30" fill="#e4efd9" stroke="#7db548" stroke-width="2"/>
      <circle cx="203" cy="33" r="28" fill="#ffffff" stroke="#5d9e31" stroke-width="5"/>
    </svg>
  </section>
</div>
</body>
</html>
```